Business Card Design Project

Business card for new event planning company. I will load in 2 different colors of logs for you to use.

Target Market(s)

meeting planners and business leaders

Industry/Entity Type

Event Planning

Requirements
Must have
• memorable/ creative please - maybe logo on back of the card

Information for business card: (Information may change)

LaVonna Birchwell
lav@MarigoldOccasionsandGatherings.com
www.MarigoldOccasionsandGatherings.com
555.730.2964
Nice to have
• Do you think it would be too much to add twiiter, FB, linked in logo to card to connect?

all are LaVonna Birchwell

```html
<!DOCTYPE html>
<html lang="en">
<head>
<meta charset="utf-8">
<title>LaVonna Birchwell – Business Card</title>
<link rel="stylesheet" href="https://fonts.googleapis.com/css2?family=Lobster&family=Mulish:wght@300;400&display=swap">
<style>
  :root {
    --lavender: #8288c0;
    --paper: #ffffff;
    --ink: #1c1c1c;
    --page: #ffffff;
    --shadow: rgba(0, 0, 0, 0.16);
  }
  * { margin: 0; padding: 0; box-sizing: border-box; }
  html, body {
    width: 1200px;
    height: 849px;
    overflow: hidden;
    background: var(--page);
  }
  .canvas {
    position: relative;
    width: 1200px;
    height: 849px;
  }
  .card {
    position: absolute;
    left: 358px;
    width: 474px;
    box-shadow: 6px 8px 18px var(--shadow);
  }
  .card--front {
    top: 72px;
    height: 300px;
    background: var(--paper);
  }
  .card--back {
    top: 447px;
    height: 301px;
    background: var(--lavender);
  }
  .front__band {
    height: 44px;
    background: var(--lavender);
  }
  .front__name {
    position: absolute;
    left: 40px;
    top: 68px;
    font-family: "Lobster", cursive;
    font-size: 44px;
    font-weight: 400;
    color: var(--lavender);
    letter-spacing: 0.2px;
  }
  .contact {
    position: absolute;
    left: 35px;
    display: flex;
    align-items: center;
    gap: 6px;
    font-family: "Mulish", sans-serif;
    font-size: 15px;
    font-weight: 300;
    color: var(--ink);
  }
  .contact__icon { width: 18px; height: 18px; flex: none; }
  .contact__domain { font-weight: 400; }
  .contact--phone { top: 168px; }
  .contact--email { top: 229px; }
  .contact--web { top: 254px; }
  .back__wordmark {
    position: absolute;
    right: 38px;
    top: 140px;
    font-family: "Mulish", sans-serif;
    font-size: 20px;
    font-weight: 400;
    color: var(--paper);
    white-space: nowrap;
  }
</style>
</head>
<body>
<main class="canvas">
  <section class="card card--front">
    <div class="front__band"></div>
    <h1 class="front__name">LaVonna Birchwell</h1>

    <p class="contact contact--phone">
      <svg class="contact__icon" viewBox="0 0 18 18" aria-hidden="true">
        <rect x="4" y="0" width="10" height="18" rx="2" fill="var(--lavender)"/>
        <rect x="5.5" y="2" width="7" height="12" fill="#b9bde0"/>
      </svg>
      555.730.2964
    </p>

    <p class="contact contact--email">
      <svg class="contact__icon" viewBox="0 0 18 18" aria-hidden="true">
        <rect x="0" y="4" width="18" height="11" fill="var(--lavender)"/>
        <path d="M0 4 L9 11 L18 4" fill="none" stroke="#ffffff" stroke-width="1"/>
      </svg>
      <span>lav@<span class="contact__domain">MarigoldOccasionsandGatherings</span>.com</span>
    </p>

    <p class="contact contact--web">
      <svg class="contact__icon" viewBox="0 0 18 18" aria-hidden="true">
        <circle cx="9" cy="9" r="8.5" fill="var(--lavender)"/>
        <path d="M4 6 Q7 4 8 7 T6 12 M11 3 Q14 7 12 10 T14 15" fill="none" stroke="#b9bde0" stroke-width="1.4"/>
      </svg>
      <span>www.<span class="contact__domain">MarigoldOccasionsandGatherings</span>.com</span>
    </p>
  </section>

  <section class="card card--back">
    <p class="back__wordmark">Marigold Occasions &amp; Gatherings</p>
  </section>
</main>
</body>
</html>
```